Yard sign

Looking for a yard sign. <br/>Something simple, name, number. <br/>Large text, readable from 50 feet away. <br/><br/>18 x 24 inches.

Target Market(s)

Potential homeowners thinking about going solar.

Colors

Designer to choose colors to be used in the design.

Requirements
Must have
• "WE'VE GONE SOLAR!"
Nice to have
• We are a solar company, we would like a design that compliments the homeowners decision that they went solar and encourages others to do the same.

```html
<!DOCTYPE html>
<html lang="en">
<head>
<meta charset="utf-8">
<title>Skyline Solar — Yard Sign Presentation</title>
<link rel="stylesheet" href="https://fonts.googleapis.com/css2?family=Anton&family=League+Gothic&family=Montserrat:wght@300;400;800;900&display=swap">
<style>
  :root {
    --board-grey: #a3a3a3;
    --label-dark: #1e1e1e;
    --sun-orange: #f68d24;
    --sun-orange-deep: #e5821f;
    --sun-yellow: #fdc82e;
    --ink: #262626;
    --bar-black: #161616;
    --white: #ffffff;
  }
  * { margin: 0; padding: 0; box-sizing: border-box; }
  html, body { width: 1200px; height: 848px; overflow: hidden; background: var(--board-grey); }
  .board { position: relative; width: 1200px; height: 848px; background: var(--board-grey); font-family: "Montserrat", sans-serif; }

  .brand-mark { display: flex; align-items: center; justify-content: center; gap: 10px; position: absolute; }
  .brand-mark__dot { border-radius: 50%; flex: none; }
  .brand-mark__name { font-family: "Montserrat", sans-serif; font-weight: 800; white-space: nowrap; line-height: 1; }

  /* Portrait sign */
  .sign-portrait {
    position: absolute; left: 41px; top: 62px; width: 543px; height: 725px;
    background: var(--sun-yellow); box-shadow: 2px 3px 6px rgba(0,0,0,.3);
  }
  .sign-portrait__panel { position: absolute; left: 10px; right: 10px; top: 0; bottom: 14px; background: var(--white); }
  .sign-portrait__header { position: absolute; left: 0; top: 0; width: 543px; height: 160px; }
  .sign-portrait .brand-mark { left: 0; right: 0; top: 66px; }
  .sign-portrait .brand-mark__dot { width: 34px; height: 34px; background: var(--white); }
  .sign-portrait .brand-mark__name { color: var(--white); font-size: 30px; }
  .sign-portrait__company {
    position: absolute; left: 0; right: 0; top: 161px; text-align: center;
    font-family: "League Gothic", sans-serif; font-size: 96px; line-height: 1; color: var(--sun-orange);
    letter-spacing: 2px;
  }
  .sign-portrait__headline {
    position: absolute; left: 0; right: 0; top: 271px; text-align: center;
    font-family: "Montserrat", sans-serif; font-weight: 900; color: var(--ink);
    font-size: 124px; line-height: 103px; letter-spacing: -2px;
  }
  .sign-portrait__callbar {
    position: absolute; left: 10px; right: 10px; top: 602px; height: 109px;
    background: linear-gradient(90deg, #121212, #262626 50%, #121212);
    display: flex; align-items: center; padding-left: 18px; gap: 14px;
  }
  .sign-portrait__phone-icon { width: 30px; height: 74px; flex: none; }
  .sign-portrait__number {
    font-family: "League Gothic", sans-serif; color: var(--white); font-size: 104px; line-height: 1;
    letter-spacing: 4px;
  }

  /* Brand showcase */
  .brand-showcase .brand-mark { left: 640px; width: 420px; top: 118px; gap: 18px; }
  .brand-showcase .brand-mark__dot { width: 90px; height: 90px; background: var(--white); }
  .brand-showcase .brand-mark__name { color: var(--white); font-size: 50px; }
  .brand-showcase__caption {
    position: absolute; left: 640px; width: 480px; top: 282px; text-align: center;
    font-weight: 300; font-size: 26px; color: var(--white); letter-spacing: .5px;
  }

  /* Landscape sign */
  .sign-landscape {
    position: absolute; left: 617px; top: 379px; width: 543px; height: 408px;
    background: var(--sun-yellow); box-shadow: 2px 3px 6px rgba(0,0,0,.3);
  }
  .sign-landscape__top { position: absolute; left: 10px; right: 10px; top: 8px; height: 96px; background: var(--white); }
  .sign-landscape .brand-mark { left: 0; right: 0; top: 36px; }
  .sign-landscape .brand-mark__dot { width: 24px; height: 24px; background: var(--sun-yellow); }
  .sign-landscape .brand-mark__name { color: var(--sun-orange); font-size: 22px; }
  .sign-landscape__field {
    position: absolute; left: 10px; right: 10px; top: 104px; height: 228px; background: var(--sun-orange);
  }
  .sign-landscape__headline {
    position: absolute; left: 0; right: 0; top: 4px; text-align: center;
    font-family: "Anton", sans-serif; font-size: 116px; line-height: 102px; color: var(--white);
    letter-spacing: -1px;
    -webkit-text-stroke: 2px #000;
    text-shadow: 4px 4px 0 #000;
  }
  .sign-landscape__callbar {
    position: absolute; left: 10px; right: 10px; top: 332px; height: 68px;
    background: linear-gradient(90deg, #121212, #2a2a2a 50%, #121212);
    display: flex; align-items: center; justify-content: center;
    font-weight: 800; font-size: 46px; letter-spacing: -1px; line-height: 1;
  }
  .sign-landscape__call-label { color: var(--sun-yellow); margin-right: 14px; }
  .sign-landscape__number { color: var(--white); }

  .board-label { position: absolute; top: 800px; font-size: 17px; font-weight: 400; color: var(--label-dark); letter-spacing: .3px; }
  .board-label--portrait { left: 39px; }
  .board-label--landscape { left: 624px; }
</style>
</head>
<body>
<main class="board">

  <section class="sign-portrait" aria-label="Portrait yard sign">
    <div class="sign-portrait__panel"></div>
    <svg class="sign-portrait__header" viewBox="0 0 543 160" aria-hidden="true">
      <defs>
        <linearGradient id="headerOrange" x1="0" x2="1" y1="0" y2="0">
          <stop offset="0" stop-color="#e5821f"/>
          <stop offset=".5" stop-color="#f68d24"/>
          <stop offset="1" stop-color="#e5821f"/>
        </linearGradient>
      </defs>
      <path d="M0 0 H543 V100 Q271.5 206 0 100 Z" fill="url(#headerOrange)"/>
    </svg>
    <div class="brand-mark">
      <span class="brand-mark__dot"></span>
      <span class="brand-mark__name">SKYLINE SOLAR</span>
    </div>
    <h2 class="sign-portrait__company">SKYLINE SOLAR</h2>
    <h1 class="sign-portrait__headline">WE'VE<br>GONE<br>SOLAR</h1>
    <div class="sign-portrait__callbar">
      <svg class="sign-portrait__phone-icon" viewBox="0 0 30 74" aria-hidden="true">
        <path d="M22 2 L29 10 L22 22 L16 22 Q12 37 16 52 L22 52 L29 64 L22 72 Q4 62 3 37 Q4 12 22 2 Z" fill="#fdc82e"/>
      </svg>
      <span class="sign-portrait__number">555-014-2290</span>
    </div>
  </section>

  <section class="brand-showcase" aria-label="Brand name">
    <div class="brand-mark">
      <span class="brand-mark__dot"></span>
      <span class="brand-mark__name">SKYLINE SOLAR</span>
    </div>
    <p class="brand-showcase__caption">YARD SIGN_DESIGN</p>
  </section>

  <section class="sign-landscape" aria-label="Landscape yard sign">
    <div class="sign-landscape__top">
      <div class="brand-mark">
        <span class="brand-mark__dot"></span>
        <span class="brand-mark__name">SKYLINE SOLAR</span>
      </div>
    </div>
    <div class="sign-landscape__field">
      <h1 class="sign-landscape__headline">WE'VE<br>GONE SOLAR</h1>
    </div>
    <div class="sign-landscape__callbar">
      <span class="sign-landscape__call-label">CALL:</span>
      <span class="sign-landscape__number">555-014-2290</span>
    </div>
  </section>

  <p class="board-label board-label--portrait">POTRAIT _YARD SIGN</p>
  <p class="board-label board-label--landscape">LANDSCAPE _YARD SIGN</p>

</main>
</body>
</html>
```